Binary Options Robot Landing Page

I need a landing page for a campaign advertising binary options robot trading. The campaign and overall look and feel should be inspired by this brand: https://quellmarktrader.com/

The screenshots you want to add from the trading area you can simple google. We will replace any screenshots with actual screenshots from our binary trading software.

You can also copy the text since we will replace the text as well.

The name to advertise is "Vextra Pilot - Bright Paths" and will be featured on www.vextrapilot.ws

What is important is the overall look!
- Vextra Pilot
- Clean Design
- Nice colors
- Makes you want to signup and trade!

Target Market(s)

People who wants to earn some extra money by investing and trading options online.

Industry/Entity Type

Advertising

Logo Text

VExtraPilot - Bright Path

Number of Pages Required

1 page

Colors

Designer to choose colors to be used in the design.

Requirements
Must have
• New Logo or remake of current logo
• Design for web resolution
• Design for mobile resolution
• Signup form as attached but designed more flashy!
• The chat popup may not block crucial elements of the design
Nice to have
• Screenshots that makes people interested to signup
• Catchy phrases that will get people interested in the product
• You are allowed to copy or partly copy the current logo
• Design a contact page
Should not have
• US flags

```html
<!DOCTYPE html>
<html lang="en">
<head>
<meta charset="utf-8">
<title>Vextra Pilot - Bright Paths</title>
<link rel="stylesheet" href="https://fonts.googleapis.com/css2?family=Exo+2:wght@600;700&family=Open+Sans:wght@400;600;700&display=swap">
<style>
:root{
  --navy:#0d3560;
  --navy-deep:#062a4f;
  --orange:#f0622a;
  --ink:#1d1d1d;
  --muted:#6b6b6b;
  --line:#e4e4e4;
  --row:#f6f6f6;
  --tab-dark:#1b1d20;
  --white:#ffffff;
}
*{box-sizing:border-box;margin:0;padding:0}
html,body{width:1200px;height:2715px;overflow:hidden;background:var(--white)}
body{position:relative;font-family:"Open Sans",Arial,sans-serif;color:var(--ink)}
.abs{position:absolute}
.heading{font-family:"Exo 2",Arial,sans-serif;font-weight:700;text-transform:uppercase;text-align:center;letter-spacing:1px}
.lead{font-size:12.5px;line-height:22px;color:var(--muted);text-align:center}

/* header */
.site-header{left:0;top:0;width:1200px;height:75px;background:var(--white)}
.brand{left:130px;top:20px;font-family:"Exo 2",Arial,sans-serif;font-weight:700;font-size:25px;color:var(--navy);letter-spacing:.5px}
.nav{left:530px;top:28px;display:flex;gap:0;font-family:"Exo 2",Arial,sans-serif;font-weight:600;font-size:11.5px;color:var(--ink)}
.nav a{color:inherit;text-decoration:none;text-transform:uppercase;position:absolute;white-space:nowrap}
.nav .active{color:var(--navy)}
.login{left:998px;top:21px;width:70px;height:34px;border-radius:17px;background:var(--orange);color:var(--white);font-family:"Exo 2",Arial,sans-serif;font-weight:700;font-size:11px;display:flex;align-items:center;justify-content:center}
.header-rule{left:0;top:75px;width:1200px;height:5px;background:var(--navy-deep)}

/* hero */
.hero{left:0;top:80px;width:1200px;height:660px;background:radial-gradient(ellipse at 50% 40%,#27486a 0%,#0e1a2a 35%,#05080d 70%)}
.hero-title{left:150px;top:310px;font-family:"Exo 2",Arial,sans-serif;font-weight:700;font-size:31px;color:var(--white)}
.hero-text{left:150px;top:375px;width:420px;font-size:13px;line-height:24px;font-weight:600;color:var(--white)}
.signup{left:771px;top:176px;width:297px;height:331px;background:rgba(8,16,26,.88)}
.signup-title{height:50px;background:var(--navy);border-bottom:3px solid var(--orange);color:var(--white);font-family:"Exo 2",Arial,sans-serif;font-weight:700;font-size:17px;display:flex;align-items:center;justify-content:center;letter-spacing:.5px}
.field{position:absolute;height:36px;border:1px solid #c8c8c8;border-radius:2px;color:var(--white);font-size:11px;padding-left:12px;display:flex;align-items:center}
.signup-btn{position:absolute;left:80px;top:268px;width:138px;height:41px;border-radius:21px;background:var(--orange);color:var(--white);font-family:"Exo 2",Arial,sans-serif;font-weight:700;font-size:11px;display:flex;align-items:center;justify-content:center}
.dot{width:15px;height:15px;border-radius:50%;border:2px solid var(--white);top:604px}
.dot.on{background:var(--orange);border-color:var(--orange)}

/* features */
.features-title{left:0;top:705px;width:1200px;font-size:25px}
.features-lead{left:230px;top:740px;width:740px}
.media{background:linear-gradient(160deg,#d9dde2,#1c4b7a 45%,#9aa3ab)}
.feature{left:530px;width:540px}
.icon-ring{position:absolute;left:0;top:0;width:62px;height:62px;border-radius:50%;border:2px solid var(--navy);display:flex;align-items:center;justify-content:center}
.feature h3{position:absolute;left:84px;top:2px;font-size:12px;font-weight:700}
.feature p{position:absolute;left:84px;top:24px;width:440px;font-size:11px;line-height:21px;color:var(--muted)}
.scroll-track{left:1060px;top:812px;width:4px;height:245px;background:#e6e6e6}
.scroll-thumb{left:1060px;top:945px;width:4px;height:40px;background:var(--navy)}

/* table */
.trading-panel{left:132px;top:1192px;width:936px;height:283px;border:1px solid var(--line)}
.tabs{display:flex;height:53px}
.tab{flex:1;display:flex;align-items:center;justify-content:center;color:var(--white);font-size:13px;background:var(--tab-dark)}
.tab.active{background:var(--navy)}
.grid-row{display:grid;grid-template-columns:160px 130px 170px 150px 160px 166px;align-items:center;text-align:center;font-size:11px;color:var(--muted)}
.grid-head{height:50px;font-weight:600;color:var(--ink)}
.grid-body{height:59px;border-top:1px solid var(--line)}
.grid-body:nth-child(odd){background:var(--row)}
.broker{font-size:17px;font-weight:600;color:#333;display:flex;align-items:center;justify-content:center;gap:6px}
.broker i{display:inline-block;width:12px;height:12px;background:#333}
.switch{margin:0 auto;width:66px;height:28px;border-radius:14px;background:var(--white);border:1px solid #ddd;position:relative}
.switch span{position:absolute;left:0;top:0;width:38px;height:26px;border-radius:13px;background:var(--orange);color:var(--white);font-size:10px;display:flex;align-items:center;justify-content:center}
.deposit{margin:0 auto;width:72px;height:26px;border-radius:13px;background:var(--navy);color:var(--white);font-size:10px;display:flex;align-items:center;justify-content:center}

/* advantages */
.adv-title{left:0;top:1532px;width:1200px;font-size:25px}
.adv-lead{left:230px;top:1567px;width:740px}
.adv-divider-v{left:380px;top:1665px;width:1px;height:395px;background:var(--line)}
.adv-divider-h{left:132px;top:1858px;width:493px;height:1px;background:var(--line)}
.adv-item{width:250px;text-align:center}
.adv-item h4{font-size:12px;font-weight:700;margin-top:8px}
.adv-item p{font-size:10.5px;line-height:20px;color:var(--muted);margin-top:6px;padding:0 6px}
.cta{left:132px;top:2087px;width:158px;height:45px;border-radius:23px;background:var(--navy);color:var(--white);font-family:"Exo 2",Arial,sans-serif;font-weight:700;font-size:11px;display:flex;align-items:center;justify-content:center}

/* steps */
.steps{left:0;top:2238px;width:1200px;height:377px;background:var(--navy)}
.steps-title{left:0;top:2298px;width:1200px;font-size:25px;color:var(--white)}
.steps-lead{left:230px;top:2333px;width:740px;color:var(--white)}
.step-line{left:383px;top:2462px;width:437px;height:6px;background:var(--white)}
.step{width:140px;height:140px;border-radius:50%;border:3px solid var(--white);background:var(--navy);top:2395px;display:flex;align-items:center;justify-content:center}
.badge{width:38px;height:38px;border-radius:50%;background:var(--orange);border:3px solid var(--white);color:var(--white);font-weight:700;font-size:14px;display:flex;align-items:center;justify-content:center;top:2380px}
.step-label{top:2533px;width:220px;text-align:center;color:var(--white);font-size:13px;font-weight:700}

/* footer */
.footer-links{left:132px;top:2640px;font-size:10px;color:#444;word-spacing:4px}
.copyright{left:132px;top:2676px;font-size:9.5px;color:#444}
.connect{left:868px;top:2653px;font-size:9.5px;color:#444}
.social{top:2645px;width:25px;height:25px;border-radius:50%;border:1px solid var(--navy)}
</style>
</head>
<body>

<header class="abs site-header">
  <div class="abs brand">VEXTRA PILOT</div>
  <nav class="abs nav">
    <a class="active" style="left:0">Home</a>
    <a style="left:70px">About Us</a>
    <a style="left:162px">Services</a>
    <a style="left:265px">FAQ</a>
    <a style="left:332px">Guides</a>
    <a style="left:414px">Contact</a>
  </nav>
  <svg class="abs" style="left:536px;top:68px" width="14" height="8"><polygon points="0,8 7,0 14,8" fill="#062a4f"/></svg>
  <div class="abs login">LOGIN</div>
</header>
<div class="abs header-rule"></div>

<section class="abs hero" role="img" aria-label="Hand touching a smartphone showing trading charts on a dark background"></section>
<h1 class="abs hero-title">Vextra Pilot - Bright Paths</h1>
<p class="abs hero-text">Lorem ipsum dolor sit amet, consectetur adipiscing elit, sed do eiusmod tempor incididunt labore et dolore...</p>

<form class="abs signup">
  <div class="signup-title">ACCOUNT INFORMATION</div>
  <div class="field" style="left:25px;top:66px;width:247px">First Name</div>
  <div class="field" style="left:25px;top:114px;width:247px">Last Name</div>
  <div class="field" style="left:25px;top:162px;width:247px">Valid E-mail Address</div>
  <div class="field" style="left:25px;top:211px;width:118px">+345</div>
  <div class="field" style="left:153px;top:211px;width:119px">Phone</div>
  <div class="signup-btn">CONTACT US</div>
</form>

<div class="abs dot on" style="left:990px"></div>
<div class="abs dot" style="left:1022px"></div>
<div class="abs dot" style="left:1054px"></div>

<svg class="abs" style="left:0;top:620px" width="1200" height="120">
  <path d="M0,120 L0,80 Q600,-20 1200,80 L1200,120 Z" fill="#ffffff"/>
  <path d="M40,105 Q600,-15 1160,105" fill="none" stroke="#f0622a" stroke-width="3"/>
</svg>

<h2 class="abs heading features-title">Features to Vextra Pilot</h2>
<p class="abs lead features-lead">Lorem ipsum dolor sit amet, consectetur adipiscing elit, sed do eiusmod tempor incididunt ut labore et dolore magna aliqua. Ut enim ad minim veniam, quis nostrud exercitation ullamco laboris nisi</p>

<div class="abs media" style="left:130px;top:792px;width:325px;height:338px;border-radius:6px" role="img" aria-label="Desktop monitor showing a trading chart with a globe"></div>

<div class="abs feature" style="top:835px">
  <div class="icon-ring"><svg width="26" height="26" viewBox="0 0 24 24"><path d="M3 10h4v11H3zM9 21h9l3-8v-3h-7l1-5-2-2-5 6z" fill="#0d3560"/></svg></div>
  <h3>Safe &amp; Secure - Automatic stop loss</h3>
  <p>Lorem Ipsum is simply dummy text of the printing and typesetting industry. Lorem Ipsum has been the industry's occaecat cupidatat...</p>
</div>
<div class="abs feature" style="top:931px">
  <div class="icon-ring"><span style="font-size:28px;font-weight:700;color:var(--navy)">$</span></div>
  <h3>No Downloads - No Charges</h3>
  <p>Lorem Ipsum is simply dummy text of the printing and typesetting industry. Lorem Ipsum has been the industry's occaecat cupidatat...</p>
</div>
<div class="abs feature" style="top:1029px">
  <div class="icon-ring"><svg width="24" height="24" viewBox="0 0 24 24"><path d="M6 3h12v5a6 6 0 0 1-12 0zM10 14h4v4h3v3H7v-3h3z" fill="#0d3560"/></svg></div>
  <h3>Trusted Vextra Pilot</h3>
  <p>Lorem Ipsum is simply dummy text of the printing and typesetting industry. Lorem Ipsum has been the industry's occaecat cupidatat...</p>
</div>
<div class="abs scroll-track"></div>
<div class="abs scroll-thumb"></div>

<section class="abs trading-panel">
  <div class="tabs"><div class="tab active">Robot Settings</div><div class="tab">History</div><div class="tab">Profile</div></div>
  <div class="grid-row grid-head"><span>Brokers</span><span>Balance</span><span>Open Trades</span><span>Profit</span><span>Active Trading</span><span>Deposit</span></div>
  <div>
    <div class="grid-row grid-body"><span class="broker"><i></i>Norvane</span><span>£8,459.50</span><span>£0</span><span>£2,567.00</span><div class="switch"><span>ON</span></div><div class="deposit">DEPOST</div></div>
    <div class="grid-row grid-body"><span class="broker"><i></i>Norvane</span><span>£8,459.50</span><span>£0</span><span>£2,567.00</span><div class="switch"><span>ON</span></div><div class="deposit">DEPOST</div></div>
    <div class="grid-row grid-body"><span class="broker"><i></i>Norvane</span><span>£8,459.50</span><span>£0</span><span>£2,567.00</span><div class="switch"><span>ON</span></div><div class="deposit">DEPOST</div></div>
  </div>
</section>

<h2 class="abs heading adv-title">Vextra Pilot Trading Advantages</h2>
<p class="abs lead adv-lead">Lorem ipsum dolor sit amet, consectetur adipiscing elit, sed do eiusmod tempor incididunt ut labore et dolore magna aliqua. Ut enim ad minim veniam, quis nostrud exercitation ullamco laboris nisi</p>

<div class="abs adv-divider-v"></div>
<div class="abs adv-divider-h"></div>

<div class="abs adv-item" style="left:130px;top:1688px">
  <svg width="60" height="54" viewBox="0 0 60 54"><polygon points="30,2 58,52 2,52" fill="#f0622a"/><rect x="27" y="18" width="6" height="20" fill="#fff"/><rect x="27" y="42" width="6" height="6" fill="#fff"/></svg>
  <h4>No Emotions</h4>
  <p>Lorem ipsum dolor sit amet, consectetur adipiscing elit, sed do eiusmod tempor incididunt ut labore et dolore magna...</p>
</div>
<div class="abs adv-item" style="left:385px;top:1688px">
  <svg width="50" height="54" viewBox="0 0 50 54"><rect x="23" y="0" width="4" height="8" fill="#f0622a"/><rect x="8" y="8" width="34" height="26" rx="8" fill="#f0622a"/><circle cx="18" cy="20" r="4" fill="#fff"/><circle cx="32" cy="20" r="4" fill="#fff"/><rect x="12" y="36" width="26" height="16" rx="4" fill="#f0622a"/></svg>
  <h4>Sequence</h4>
  <p>Lorem ipsum dolor sit amet, consectetur adipiscing elit, sed do eiusmod tempor incididunt ut labore et dolore magna...</p>
</div>
<div class="abs adv-item" style="left:130px;top:1886px">
  <svg width="62" height="54" viewBox="0 0 62 54"><path d="M16 40a12 12 0 0 1 0-24 16 16 0 0 1 30 0 12 12 0 0 1 0 24z" fill="#f0622a"/><path d="M27 22h8v10h6L31 44 21 32h6z" fill="#fff"/></svg>
  <h4>No Download</h4>
  <p>Lorem ipsum dolor sit amet, consectetur adipiscing elit, sed do eiusmod tempor incididunt ut labore et dolore magna...</p>
</div>
<div class="abs adv-item" style="left:385px;top:1886px">
  <svg width="56" height="54" viewBox="0 0 56 54"><rect x="4" y="10" width="40" height="40" fill="none" stroke="#f0622a" stroke-width="5"/><path d="M44 2l8 8-24 24-10 2 2-10z" fill="#f0622a"/></svg>
  <h4>Ability to Open VIP Account</h4>
  <p>Lorem ipsum dolor sit amet, consectetur adipiscing elit, sed do eiusmod tempor incididunt ut labore et dolore magna...</p>
</div>

<div class="abs media" style="left:670px;top:1650px;width:400px;height:500px;border-radius:8px;background:linear-gradient(160deg,#f3f4f7,#c9ccd6 50%,#8a8f9c)" role="img" aria-label="White robot figure holding a software window"></div>

<div class="abs cta">GET STARTED TODAY</div>

<section class="abs steps"></section>
<h2 class="abs heading steps-title">Get Started in 3 Easy Steps</h2>
<p class="abs lead steps-lead">Lorem ipsum dolor sit amet, consectetur adipiscing elit, sed do eiusmod tempor incididunt ut labore et dolore magna aliqua. Ut enim ad minim veniam, quis nostrud exercitation ullamco laboris nisi</p>
<div class="abs step-line"></div>

<div class="abs step" style="left:243px"><svg width="46" height="52" viewBox="0 0 46 52"><circle cx="23" cy="13" r="12" fill="#fff"/><path d="M2 52a21 21 0 0 1 42 0z" fill="#fff"/></svg></div>
<div class="abs step" style="left:532px"><svg width="46" height="56" viewBox="0 0 46 56"><path d="M15 2h16l-5 10h-6z" fill="#fff"/><path d="M18 14h10c12 8 18 20 18 30 0 8-6 12-12 12H12C6 56 0 52 0 44c0-10 6-22 18-30z" fill="#fff"/><text x="23" y="47" text-anchor="middle" font-family="Open Sans,Arial,sans-serif" font-weight="700" font-size="22" fill="#0d3560">$</text></svg></div>
<div class="abs step" style="left:820px"><svg width="56" height="50" viewBox="0 0 56 50"><rect x="8" y="42" width="26" height="8" fill="#fff"/><path d="M18 42l6-20 18-12" fill="none" stroke="#fff" stroke-width="6"/><circle cx="24" cy="22" r="5" fill="#fff"/><path d="M42 4l10 4-4 10" fill="none" stroke="#fff" stroke-width="4"/></svg></div>

<div class="abs badge" style="left:336px">1</div>
<div class="abs badge" style="left:623px">2</div>
<div class="abs badge" style="left:910px">3</div>

<div class="abs step-label" style="left:203px">Open a free account</div>
<div class="abs step-label" style="left:492px">Deposit (no fees!)</div>
<div class="abs step-label" style="left:780px">Begin robot trading!</div>

<footer>
  <div class="abs footer-links">HOME &nbsp;| &nbsp;ABOUT US &nbsp;| &nbsp;SERVICES &nbsp;| &nbsp;FAQ &nbsp;| &nbsp;GUIDES &nbsp;| &nbsp;CONTACT</div>
  <div class="abs copyright">COPYRIGHTS © VEXTRAPILOT , 2017 | ALL RIGHTS RESERVED.</div>
  <div class="abs connect">CONNECT WITH US :</div>
  <div class="abs social" style="left:959px"></div>
  <div class="abs social" style="left:987px"></div>
  <div class="abs social" style="left:1015px"></div>
  <div class="abs social" style="left:1043px"></div>
</footer>

</body>
</html>
```